Leadership Seminar Concept

We want the theme picture/design of the Leadership Seminar Flyer with theme "Inspiring Commitment"

Industry/Entity Type

Leadership

```html
<!DOCTYPE html>
<html lang="en">
<head>
<meta charset="utf-8">
<title>Inspiring Commitment – Leadership Seminar Flyer</title>
<link href="https://fonts.googleapis.com/css2?family=Oswald:wght@200;300;600;700&family=Open+Sans:wght@400;600;700&display=swap" rel="stylesheet">
<style>
  :root {
    --plum: #7d1a52;
    --ink: #2a2a2a;
    --grey-ink: #444444;
    --blue: #1f7fc0;
    --gold: #f2b705;
    --paper: #f4f4f5;
    --backdrop: #d2d2d2;
    --white: #ffffff;
  }
  * { box-sizing: border-box; margin: 0; padding: 0; }
  html, body { width: 1200px; height: 800px; overflow: hidden; }
  body {
    background: var(--backdrop);
    display: flex;
    align-items: center;
    justify-content: center;
    font-family: "Open Sans", sans-serif;
  }
  .flyer {
    position: relative;
    width: 540px;
    height: 760px;
    background: var(--paper);
    overflow: hidden;
  }
  .flyer__photo {
    position: absolute;
    inset: 0;
    background:
      radial-gradient(ellipse 150px 110px at 400px 420px, rgba(38,160,200,0.85), rgba(38,160,200,0) 100%),
      radial-gradient(ellipse 200px 140px at 170px 300px, rgba(225,228,236,0.9), rgba(225,228,236,0) 100%),
      linear-gradient(180deg, #fbfbfc 0%, #eceef1 55%, #e9eaec 100%);
  }
  .title {
    position: absolute;
    top: 68px;
    right: 40px;
    text-align: right;
    font-family: "Oswald", sans-serif;
    line-height: 0.95;
  }
  .title__bold { display: block; color: var(--plum); font-weight: 700; font-size: 42px; }
  .title__light { display: block; color: var(--grey-ink); font-weight: 200; font-size: 40px; }
  .headline {
    position: absolute;
    top: 112px;
    left: 14px;
    width: 182px;
    padding: 8px 8px 10px 4px;
    border: 1px solid var(--plum);
    text-align: right;
    font-family: "Oswald", sans-serif;
    font-weight: 300;
    font-size: 27px;
    line-height: 0.93;
    color: var(--ink);
    text-transform: uppercase;
  }
  .headline strong { color: var(--plum); font-weight: 600; }
  .columns {
    position: absolute;
    top: 470px;
    left: 40px;
    right: 40px;
    display: grid;
    grid-template-columns: 150px 140px;
    column-gap: 40px;
    font-size: 10.5px;
    line-height: 1.28;
    color: var(--grey-ink);
  }
  .columns p strong { font-weight: 700; }
  .column--commitment strong { color: var(--plum); }
  .column--shiftability strong { color: var(--blue); }
  .invite {
    position: absolute;
    left: 0;
    right: 0;
    bottom: 0;
    height: 74px;
    background: var(--plum);
    color: var(--white);
    padding: 14px 40px;
    font-size: 13px;
    line-height: 1.35;
  }
  .invite__initial { color: var(--gold); font-weight: 700; font-size: 22px; line-height: 1; }
</style>
</head>
<body>
  <article class="flyer">
    <div class="flyer__photo" role="img" aria-label="Photograph of a blue paper boat leading a row of white paper boats on a pale surface"></div>

    <h1 class="title">
      <span class="title__bold">INSPIRING</span>
      <span class="title__light">COMMITMENT</span>
    </h1>

    <h2 class="headline">
      Shifting <strong>self,</strong><br>
      your <strong>people</strong><br>
      and your<br>
      <strong>organization</strong><br>
      from <strong>static</strong> to<br>
      <strong>movement</strong> to<br>
      <strong>momentum</strong>
    </h2>

    <section class="columns">
      <p class="column--commitment"><strong>Inspiring commitment is enabling others to act.</strong> It involves energizing individuals to strive towards a compelling vision of the future, guiding people through change, keeping everyone aligned, building trust and open channels of communication, while reinforcing success.</p>
      <p class="column--shiftability"><strong>Shiftability is responding to outward demands from inward strength, purpose and skill.</strong> The mindset of shiftability acknowledges the need for change and embraces it, keeping an open mind about new ideas while wisely retaining things that still apply - always learning, always building, always growing.</p>
    </section>

    <footer class="invite">
      <p><span class="invite__initial">W</span>e invite you to a journey of greatness where you'll learn and practice tools for thriving as a leader by inspiring momentum.</p>
    </footer>
  </article>
</body>
</html>
```